Artist business cards needed, happy acrylic painter

I'd like a business card I can hand out to people interested in my paintings. I'd like a logo that includes elements of my painting. I have shared a collection that may be used at https://snaplink.example/photos/7xQpLmR3Tz8vBn2K
I get my vibe and the type of art I create, you can also see my active Circle Net account: https://circlesnet.example/+MarlaVintner

Target Market(s)

people interested in art

Industry/Entity Type

Artists

Contact Information for Business Card

Marla Vintner
425-736-1048
marlavintner@quillpost.com
marlavintner@quillpost.com
www.marlavintner-studio.com

Font styles to use
Sans Serif
Decorative
Script

Requirements
Must have
• 1. Colors that are represented in my paintings
• 2. Elements from my paintings: Link to the cloud locker with my art: https://snaplink.example/photos/7xQpLmR3Tz8vBn2K
• 3. Flower(s)
• 4. A box on the back that's outlined so a note could be added. I've attached a photo of a business card my friend uses for her floral design company as an example of the back of the card with the quote and a box and business name (Marla Vintner).
• 4. I'd like to have this quote on the back of the card too.
• "I must have flowers, always and always."
• ~Anton Brisle
Nice to have
• In smaller font
• If it fits, links to my other social media:
• https://circlesnet.example/+MarlaVintner
• https://www.friendwall.example/marlavintnerartist/
Should not have
• A dark background

```html
<!DOCTYPE html>
<html lang="en">
<head>
<meta charset="utf-8">
<title>Marla Vintner — Business Card</title>
<link rel="stylesheet" href="https://fonts.googleapis.com/css2?family=Dancing+Script:wght@600;700&family=Quicksand:wght@500;600&display=swap">
<style>
  :root {
    --page-bg: #ecebe6;
    --mint: #d6ebe4;
    --mint-light: #e8f4ef;
    --ink-blue: #2f6fc0;
    --teal: #2aa58c;
    --violet: #7a4fb0;
    --petal-blue: #5a86d6;
    --petal-peach: #e9b98a;
    --stem-green: #6fc8ad;
    --blush: #f1dbe6;
    --social-red: #e0513f;
    --social-blue: #3b5a9a;
    --card-white: #fdfdfc;
  }
  * { box-sizing: border-box; margin: 0; padding: 0; }
  html, body { width: 1200px; height: 950px; overflow: hidden; }
  body {
    background: var(--page-bg);
    font-family: "Quicksand", sans-serif;
    position: relative;
  }
  .card {
    position: absolute;
    border-radius: 22px;
    overflow: hidden;
    box-shadow: 0 6px 18px rgba(0,0,0,.12);
  }

  /* Front */
  .card-front {
    left: 40px; top: 280px;
    width: 640px; height: 366px;
    background: linear-gradient(160deg, var(--mint-light), var(--mint));
  }
  .front-painting {
    position: absolute; inset: 0;
    width: 100%; height: 100%;
  }
  .front-details {
    position: absolute;
    left: 52px; top: 150px;
    color: var(--ink-blue);
  }
  .artist-name {
    font-family: "Dancing Script", cursive;
    font-weight: 700;
    font-size: 44px;
    line-height: 1;
    margin-bottom: 16px;
  }
  .contact-list { list-style: none; font-size: 16px; font-weight: 500; }
  .contact-list li {
    display: flex; align-items: center; gap: 10px;
    margin-bottom: 6px;
  }
  .contact-list svg { width: 16px; height: 16px; flex: none; }

  /* Back */
  .card-back {
    left: 760px; top: 125px;
    width: 390px; height: 682px;
    background: var(--card-white);
  }
  .back-sprig {
    position: absolute; left: 150px; top: 26px;
    width: 90px; height: 52px;
    border-radius: 40% 40% 10% 10%;
    background: linear-gradient(90deg, var(--petal-peach), var(--violet), var(--petal-blue));
  }
  .back-quote {
    position: absolute; left: 0; right: 0; top: 88px;
    text-align: center;
    color: var(--ink-blue);
    font-size: 19px; font-weight: 600;
    line-height: 1.3;
    padding: 0 30px;
  }
  .note-box {
    position: absolute;
    left: 32px; top: 158px;
    width: 326px; height: 370px;
    border: 2px solid var(--teal);
    background: radial-gradient(circle at 40% 45%, var(--blush), #f7eef4 55%, #f4f8f6);
  }
  .quote-author {
    position: absolute; right: 40px; top: 548px;
    font-family: "Dancing Script", cursive;
    font-weight: 700; font-size: 30px;
    color: var(--ink-blue);
  }
  .social-row {
    position: absolute; left: 30px; bottom: 30px;
    display: flex; gap: 22px;
    font-size: 15px; font-weight: 500;
    color: var(--ink-blue);
  }
  .social-item { display: flex; align-items: center; gap: 7px; }
  .social-dot { width: 14px; height: 14px; border-radius: 50%; }
  .social-dot.circle-net { background: var(--social-red); }
  .social-dot.friend-wall { background: var(--social-blue); }
</style>
</head>
<body>

<section class="card card-front" aria-label="Business card front">
  <svg class="front-painting" viewBox="0 0 640 366" role="img" aria-label="Acrylic painting of violet, blue and peach flowers along the card's right side">
    <defs>
      <linearGradient id="flowerField" x1="1" y1="0" x2="0" y2="1">
        <stop offset="0" stop-color="#6fa9e0"/>
        <stop offset=".35" stop-color="#8a5cc0"/>
        <stop offset=".65" stop-color="#a98bc4"/>
        <stop offset="1" stop-color="#e9c79a"/>
      </linearGradient>
    </defs>
    <path d="M640 0 L640 366 L250 366 C280 320 300 280 340 250 C390 200 430 170 470 120 C510 70 540 30 560 0 Z" fill="url(#flowerField)" opacity=".85"/>
  </svg>
  <div class="front-details">
    <h1 class="artist-name">Marla Vintner</h1>
    <ul class="contact-list">
      <li>
        <svg viewBox="0 0 16 16"><rect x="1" y="1" width="14" height="14" rx="2" fill="none" stroke="currentColor" stroke-width="1.4"/><path d="M5 4h2l1 3-1.5 1a6 6 0 0 0 2.5 2.5L10 9l3 1v2a1 1 0 0 1-1 1A9 9 0 0 1 4 5a1 1 0 0 1 1-1z" fill="currentColor" transform="scale(.8) translate(2 2)"/></svg>
        425-736-1048
      </li>
      <li>
        <svg viewBox="0 0 16 16"><rect x="1" y="1" width="14" height="14" rx="2" fill="currentColor"/><path d="M3.5 5.5h9v6h-9z M3.5 5.5l4.5 3.5 4.5-3.5" fill="none" stroke="#fff" stroke-width="1.1"/></svg>
        marlavintner@quillpost.com
      </li>
      <li>
        <svg viewBox="0 0 16 16"><circle cx="8" cy="8" r="7" fill="none" stroke="currentColor" stroke-width="1.4"/><path d="M1 8h14M8 1c-3 3-3 11 0 14M8 1c3 3 3 11 0 14" fill="none" stroke="currentColor" stroke-width="1.1"/></svg>
        www.marlavintner-studio.com
      </li>
    </ul>
  </div>
</section>

<section class="card card-back" aria-label="Business card back">
  <div class="back-sprig" role="img" aria-label="Small bouquet of painted flowers"></div>
  <p class="back-quote">“I must have flowers,<br>always and always.”</p>
  <div class="note-box" role="img" aria-label="Outlined note box over a faint painted floral wash"></div>
  <p class="quote-author">~Anton Brisle</p>
  <div class="social-row">
    <span class="social-item"><span class="social-dot circle-net"></span>MarlaVintner</span>
    <span class="social-item"><span class="social-dot friend-wall"></span>/marlavintnerartist</span>
  </div>
</section>

</body>
</html>
```